Veltrisk inc. Aviation website

we are looking for a very modern and luxury web design, we are an aviation based company and specialize in aircraft exports and setup of air services world wide.
we want the website to be unique, creative, luxurious, professional, and to make an statement.
we have attached the logo.
our business cards theme is black background with gold stamping, if that is the rout you want to take.
**The format we are looking for is Wordpress.**
**the website is www.veltriskinc-example.com**
** 3 pages:
1. home page: -overview/about us
-industry leading
- worldwide presence
- aerial support
2. products and services: -business aircrafts
-commercial aircrafts
-amphibious aircrafts
-operation setup
-maintenance & crew training
3. contact us
**our location: Marlow Fenwick Harbour Airfield, Hangar 6**
we do appreciate suggestions
Thank you all.
Target Market(s)
Aviation professionals, Aircraft import/export, airlines, air taxi operations
Industry/Entity Type
It Company
Number of Pages Required
3 page
Requirements
Must have
- must have a very modern and luxurious design, and must be aviation oriented, and must have the logo, must be professional looking and be animated.
Nice to have
- black, gold, and burgandy colour
Should not have
- should not be playful and cartoony.

```html
<!DOCTYPE html>
<html lang="en">
<head>
<meta charset="utf-8">
<title>Veltrisk inc. — Aviation</title>
<link href="https://fonts.googleapis.com/css2?family=Open+Sans:wght@400;600;700&display=swap" rel="stylesheet">
<style>
:root{
  --cream:#fdfaf3;
  --sand:#f8efe0;
  --white:#ffffff;
  --burgundy:#8e1a1c;
  --gold:#a8772b;
  --gold-deep:#a56f22;
  --gold-line:#b98a4a;
  --text:#5b5b5b;
  --footer:#2b2a28;
  --footer-bar:#363532;
  --footer-text:#b9b6b0;
  --footer-head:#f1ede6;
}
*{margin:0;padding:0;box-sizing:border-box}
html,body{width:914px;height:1200px;overflow:hidden}
body{font-family:"Open Sans",Arial,sans-serif;color:var(--text);background:var(--white);position:relative}

.site-header{position:absolute;left:0;top:0;width:914px;height:72px;background:var(--cream)}
.brand{position:absolute;left:116px;top:24px;display:flex;align-items:center;gap:8px;font-size:19px;font-weight:600;color:var(--burgundy);letter-spacing:1px}
.brand-dot{width:22px;height:22px;border-radius:50%;background:var(--gold)}
.main-nav{position:absolute;top:29px;left:586px;display:flex;gap:28px;font-size:11px;font-weight:600}
.main-nav a{color:var(--burgundy);text-decoration:none}
.main-nav a.active{color:var(--gold);border-bottom:1px solid var(--gold);padding-bottom:2px}

.hero{position:absolute;left:0;top:72px;width:914px;height:317px;
  background:
    radial-gradient(ellipse 60% 45% at 18% 82%,rgba(236,150,70,.85),rgba(236,150,70,0) 70%),
    radial-gradient(ellipse 55% 40% at 85% 88%,rgba(244,186,120,.8),rgba(244,186,120,0) 70%),
    radial-gradient(ellipse 45% 35% at 62% 30%,rgba(120,160,220,.55),rgba(120,160,220,0) 70%),
    radial-gradient(ellipse 70% 50% at 40% 60%,rgba(40,50,90,.7),rgba(40,50,90,0) 75%),
    linear-gradient(180deg,#132a63 0%,#24469a 30%,#4d5f93 55%,#8a6f74 78%,#c88a52 100%)}
.hero h1{position:absolute;left:0;top:127px;width:914px;text-align:center;color:#fff;font-size:23px;font-weight:700;line-height:30px;letter-spacing:.1px;text-shadow:0 1px 4px rgba(0,0,0,.45)}
.btn{display:block;background:var(--gold);color:#fff;font-size:10px;font-weight:600;letter-spacing:.5px;text-align:center;text-decoration:none}
.hero .btn{position:absolute;left:409px;top:225px;width:96px;height:29px;line-height:29px;background:var(--gold-deep)}

.about{position:absolute;left:0;top:389px;width:914px;height:296px;background:var(--sand)}
.section-title{font-size:19px;font-weight:700;color:var(--burgundy);letter-spacing:.8px;border-bottom:1px solid var(--gold-line);padding-bottom:1px}
.about .section-title{position:absolute;left:110px;top:32px;width:356px}
.about-copy{position:absolute;left:110px;top:68px;width:358px;font-size:8.6px;line-height:11px;letter-spacing:.1px}
.about-copy p:nth-child(1){margin-bottom:11px}
.about-copy p:nth-child(2){margin-bottom:16px}
.about .btn{position:absolute;left:110px;top:228px;width:96px;height:29px;line-height:29px}
.about-photo{position:absolute;left:490px;top:39px;width:313px;height:218px;
  background:
    radial-gradient(ellipse 45% 40% at 62% 42%,rgba(210,210,210,.45),rgba(210,210,210,0) 70%),
    radial-gradient(ellipse 30% 55% at 22% 78%,rgba(20,20,20,.75),rgba(20,20,20,0) 75%),
    linear-gradient(135deg,#555 0%,#3a3a3a 55%,#262626 100%)}

.overview{position:absolute;left:0;top:685px;width:914px;height:313px;background:var(--white)}
.overview .section-title{position:absolute;left:109px;top:34px;width:695px}
.feature{position:absolute;top:72px;width:226px}
.feature-photo{width:219px;height:123px}
.feature h3{margin-top:9px;font-size:11.5px;font-weight:600;color:var(--gold);letter-spacing:.4px;position:relative;padding-bottom:5px}
.feature h3::after{content:"";position:absolute;left:0;bottom:0;width:52px;height:1px;background:var(--gold-line)}
.feature p{margin-top:14px;font-size:8.8px;line-height:14.5px;letter-spacing:.15px}

.site-footer{position:absolute;left:0;top:998px;width:914px;height:172px;background:var(--footer)}
.footer-col{position:absolute;top:24px}
.footer-col h4{font-size:9px;font-weight:600;color:var(--footer-head);letter-spacing:.4px;display:inline-block;border-bottom:1px solid #6c6760;padding-bottom:5px}
.contact-list{list-style:none;margin-top:6px}
.contact-list li{display:flex;align-items:center;gap:7px;font-size:7.5px;color:var(--footer-text);height:20.5px;letter-spacing:.2px}
.contact-list svg{width:13px;height:13px}
.footer-about p{margin-top:10px;width:150px;font-size:7.8px;line-height:14.7px;letter-spacing:.3px;color:var(--footer-text)}
.quick-links{list-style:none;margin-top:8px}
.quick-links li{font-size:8.8px;color:var(--footer-text);height:18.5px;letter-spacing:.3px}
.quick-links li::before{content:"›";color:var(--gold);margin-right:6px}
.gallery{display:grid;grid-template-columns:repeat(3,41px);gap:12px 8px;margin-top:10px}
.gallery span{display:block;height:26px;border:1px solid #d8d4cd}
.footer-bar{position:absolute;left:0;top:1170px;width:914px;height:30px;background:var(--footer-bar);text-align:center;line-height:30px;font-size:8.5px;color:var(--footer-text);letter-spacing:.3px}
</style>
</head>
<body>
<header class="site-header">
  <div class="brand"><span class="brand-dot"></span>Veltrisk</div>
  <nav class="main-nav">
    <a class="active" href="#">HOME</a>
    <a href="#">PRODUCTS</a>
    <a href="#">CONTACT US</a>
  </nav>
</header>

<section class="hero" role="img" aria-label="Passenger jet landing against a dramatic blue and orange sunset sky">
  <h1>WE ARE MANUFACTURING PRODUCTS WITH WORLD<br>CLASS QUALITY.</h1>
  <a class="btn" href="#">READ MORE</a>
</section>

<section class="about">
  <h2 class="section-title">About Us</h2>
  <div class="about-copy">
    <p>Welcome, I am happy to introduce our website ipsum dolor sit amet, consectetur adipiscing elit. Ut elit tellus, luctus nec ullamcorper mattis, pulvinar dapibus leo. I am text block. Click edit button to change this text. Lorem ipsum dolor sit amet, consectetur adipiscing elit.</p>
    <p>There are many variations of passages of Lorem Ipsum available, but the majority have suffered alteration in some form, by injected humour, or randomised words which don't look even slightly believable.</p>
    <p>Welcome, I am happy to introduce our website ipsum dolor sit amet, consectetur adipiscing elit. Ut elit tellus, luctus nec ullamcorper mattis, pulvinar dapibus leo. I am text block. Click edit button to change this text. Lorem ipsum dolor sit amet, consectetur adipiscing elit.</p>
  </div>
  <a class="btn" href="#">READ MORE</a>
  <div class="about-photo" role="img" aria-label="Businessman sketching a cloud of travel and media icons on a chalkboard"></div>
</section>

<section class="overview">
  <h2 class="section-title">Overview</h2>
  <article class="feature" style="left:110px">
    <div class="feature-photo" role="img" aria-label="Engineers in safety glasses working on machinery" style="background:radial-gradient(ellipse 50% 60% at 65% 55%,rgba(40,70,120,.7),rgba(40,70,120,0) 70%),radial-gradient(ellipse 40% 45% at 20% 30%,rgba(235,238,240,.9),rgba(235,238,240,0) 70%),linear-gradient(135deg,#d9dcde,#9aa5b0 50%,#4a5a72)"></div>
    <h3>Industry Leading</h3>
    <p>Lorem ipsum dolor sit amet,consectetur adipiscing elit. Ut elit tellus, luctus nec ullamcorper mattis, pulvinar dapibus leo.</p>
  </article>
  <article class="feature" style="left:346px">
    <div class="feature-photo" role="img" aria-label="Interior of an aircraft fuselage under construction" style="background:radial-gradient(ellipse 25% 35% at 40% 35%,rgba(225,240,250,.95),rgba(225,240,250,0) 75%),radial-gradient(ellipse 70% 60% at 50% 50%,rgba(60,110,160,0) 40%,rgba(30,60,100,.6) 100%),linear-gradient(180deg,#8fb8d8,#5d8db8 50%,#9fb0c0)"></div>
    <h3>Worldwide Presence</h3>
    <p>Lorem ipsum dolor sit amet,consectetur adipiscing elit. Ut elit tellus, luctus nec ullamcorper mattis, pulvinar dapibus leo.</p>
  </article>
  <article class="feature" style="left:585px">
    <div class="feature-photo" role="img" aria-label="Two helicopters flying over hazy terrain" style="background:radial-gradient(ellipse 50% 40% at 55% 45%,rgba(150,150,145,.6),rgba(150,150,145,0) 70%),linear-gradient(180deg,#6f7375,#5e6160 55%,#736b60)"></div>
    <h3>Aerial Support</h3>
    <p>Lorem ipsum dolor sit amet,consectetur adipiscing elit. Ut elit tellus, luctus nec ullamcorper mattis, pulvinar dapibus leo.</p>
  </article>
</section>

<footer class="site-footer">
  <div class="footer-col" style="left:110px">
    <h4>CONTACT US</h4>
    <ul class="contact-list">
      <li><svg viewBox="0 0 14 14"><path d="M7 1.5a4 4 0 0 0-4 4c0 3 4 7 4 7s4-4 4-7a4 4 0 0 0-4-4z" fill="none" stroke="#c98a3a" stroke-width="1.2"/><circle cx="7" cy="5.5" r="1.3" fill="#c98a3a"/></svg>Enter your email address to</li>
      <li><svg viewBox="0 0 14 14"><circle cx="7" cy="7" r="5.8" fill="none" stroke="#b5332e" stroke-width="1.1"/><path d="M5 4.3l1 1.5-.7.8a4 4 0 0 0 2 2l.8-.7 1.5 1-.6 1a4.5 4.5 0 0 1-4.9-4.9z" fill="#b5332e"/></svg>000+9999+0000</li>
      <li><svg viewBox="0 0 14 14"><rect x="1.5" y="3.5" width="11" height="7.5" fill="none" stroke="#c98a3a" stroke-width="1.1"/><path d="M1.5 3.5l5.5 4.3 5.5-4.3M1.5 11l4-3.5M12.5 11l-4-3.5" fill="none" stroke="#c98a3a" stroke-width="1"/></svg>hello@veltrisk-mail.com</li>
      <li><svg viewBox="0 0 14 14"><rect x="3.5" y="1.5" width="7" height="3.5" fill="#c0392b"/><rect x="1.5" y="5" width="11" height="5" rx="1" fill="#c0392b"/><rect x="3.5" y="8.5" width="7" height="4" fill="#e06a5a"/></svg>0000+888+999+66</li>
    </ul>
  </div>
  <div class="footer-col footer-about" style="left:287px">
    <h4>ABOUT US</h4>
    <p>Sed consequat interdum ullamcorp-er. Quisque interdum molestie elit, quis molestie sapien scelerisque eget. Aenean pretium dictum libero at ullamcorper. Donec tortor neque to the bricks.</p>
  </div>
  <div class="footer-col" style="left:508px">
    <h4>QUICK LINKS</h4>
    <ul class="quick-links">
      <li>Home</li>
      <li>Products</li>
      <li>Contact</li>
    </ul>
  </div>
  <div class="footer-col" style="left:662px">
    <h4>PHOTO GALLERY</h4>
    <div class="gallery">
      <span role="img" aria-label="Aircraft thumbnail" style="background:linear-gradient(180deg,#9db8d6,#2a2a2a)"></span>
      <span role="img" aria-label="Aircraft at sunset thumbnail" style="background:linear-gradient(180deg,#4a3a4a,#d0573a)"></span>
      <span role="img" aria-label="Aircraft on runway thumbnail" style="background:linear-gradient(180deg,#a9c4dc,#7f8f6a)"></span>
      <span role="img" aria-label="Pilot beside jet thumbnail" style="background:linear-gradient(180deg,#c7d3de,#8a8a86)"></span>
      <span role="img" aria-label="Business jet thumbnail" style="background:linear-gradient(180deg,#4d8dc8,#e7eef5)"></span>
      <span role="img" aria-label="Jet in flight thumbnail" style="background:linear-gradient(180deg,#3f7fbf,#d8e4ef)"></span>
      <span role="img" aria-label="Airliner thumbnail" style="background:linear-gradient(180deg,#a8b8c8,#e8ecef)"></span>
      <span role="img" aria-label="Jets over sea thumbnail" style="background:linear-gradient(180deg,#7fb3e0,#2f6aa6)"></span>
      <span role="img" aria-label="Airship thumbnail" style="background:linear-gradient(180deg,#8fa7c4,#b5c3d3)"></span>
    </div>
  </div>
</footer>
<div class="footer-bar">© 2016 veltrisk. All Rights Reserved</div>
</body>
</html>
```